A specialised Sport management needs a corporate brochure design

We are a specialized company in the management and consultancy of sports events. and need to have a company brochure
We provide the following services;
Event management
Venues management
Production
Ticketing
Consulting
Hospitality
Activity management
Event timing
Branding of event
Event supplies
We need a corporate profile design for our company to showcase the major events that we have covered , with images, information, statistics, surveys, products and services used. We want to highlight our professionalism and execution of the events, experience of the participants, spectators . How we have grown in the past few years and reached the international standards.
Objectives of the work:
To get sponsors and partners for future business and to present Keel-Marrow
as not just a sports management company but also a professional sports
events management company.
You can check our website
www.keel-marrow.example
Target Market(s)
Sponsors and corporate partners
Industry/Entity Type
Events
Font styles to use
Requirements
Must have
- Must Have:
- - Very professional look
- -Some event images,Event information, statistics, surveys, products and services used. We want to highlight our professionalism and execution of the events (Attached)
Nice to have
- Similar momentom of the below design
- http://www.dunlathgames.example/wp-content/themes/dunlath_games/pdf/CP-2014-15-V10-Web.pdf

```html
<!DOCTYPE html>
<html lang="en">
<head>
<meta charset="utf-8">
<title>Keel-Marrow – Sports Event Management</title>
<link rel="stylesheet" href="https://fonts.googleapis.com/css2?family=Bebas+Neue&family=Roboto+Condensed:wght@400;700&display=swap">
<style>
  :root {
    --sky: #f1e8de;
    --sand: #d9c9b6;
    --crowd-green: #5f8f5a;
    --crowd-dark: #4a4238;
    --band: rgba(40, 28, 20, 0.62);
    --accent-orange: #ee6a2c;
    --brand-grey: #3c3c3c;
    --text-light: #ffffff;
    --url-grey: #8a8580;
  }
  * { margin: 0; padding: 0; box-sizing: border-box; }
  html, body { width: 1200px; height: 1200px; overflow: hidden; background: var(--sky); }
  .poster {
    position: relative;
    width: 1200px;
    height: 1200px;
    overflow: hidden;
    background: var(--sky);
    font-family: "Roboto Condensed", "Arial Narrow", sans-serif;
  }
  .event-photo {
    position: absolute;
    left: 0; top: 0;
    width: 1173px; height: 1200px;
    background: linear-gradient(180deg,
      var(--sky) 0%, var(--sky) 26%,
      var(--sand) 36%,
      var(--crowd-green) 52%,
      var(--crowd-dark) 72%,
      #6b5c4c 100%);
  }
  .side-stripe {
    position: absolute;
    right: 0; top: 0;
    width: 27px; height: 1200px;
    background: var(--accent-orange);
  }
  .headline-band {
    position: absolute;
    left: 147px; top: 693px;
    width: 1026px; height: 507px;
    background: var(--band);
  }
  .site-url {
    position: absolute;
    left: 112px; top: 52px;
    writing-mode: vertical-rl;
    font-size: 15px;
    letter-spacing: 1px;
    color: var(--url-grey);
    text-transform: uppercase;
  }
  .brand {
    position: absolute;
    right: 110px; top: 110px;
    display: flex;
    align-items: center;
    gap: 14px;
  }
  .brand-dot {
    width: 26px; height: 26px;
    border-radius: 50%;
    background: var(--accent-orange);
  }
  .brand-name {
    font-family: "Roboto Condensed", "Arial Narrow", sans-serif;
    font-weight: 700;
    font-size: 46px;
    color: var(--brand-grey);
    letter-spacing: 1px;
  }
  .headline {
    position: absolute;
    right: 90px; top: 735px;
    text-align: right;
    font-family: "Bebas Neue", "Oswald", sans-serif;
    font-size: 112px;
    line-height: 91px;
    color: var(--text-light);
    letter-spacing: 1px;
  }
</style>
</head>
<body>
  <main class="poster">
    <div class="event-photo" role="img" aria-label="Runners in coloured race shirts and bibs starting a desert running event under a hazy sky"></div>
    <div class="headline-band"></div>
    <div class="side-stripe"></div>
    <p class="site-url">www.keel-marrow.example</p>
    <div class="brand">
      <span class="brand-dot"></span>
      <span class="brand-name">KEEL-MARROW</span>
    </div>
    <h1 class="headline">Let’s take<br>care of your<br>next sports<br>event!</h1>
  </main>
</body>
</html>
```